Sale PPC Banner Ad Design Update

We need some Plumora PPC Banner Ad's for our sale altered to include product shots in the background. Attached are some examples that we currently use. We want a similar format/look but with the attached product shots used as the background image. Product image is called "VKSLite Level 7"

Have also included our logo file as well.

Industry/Entity Type

Plumora

Font styles to use
Sans Serif

Requirements
Must have
• The must-have sizes (up to 150kb):
• • Banner: 468 x 60
• • Large mobile banner 320 x 100
• • Leaderboard: 728 x 90
• • Square: 250 x 250
• • Small square: 200 x 200
• • Large rectangle: 336 x 280
Nice to have
• The nice-to-have sizes:
• • Vertical rectangle: 240 x 400
• • Mobile leaderboard: 320 x 50
• • Inline rectangle: 300 x 250
• • Skyscraper: 120 x 600
• • Wide skyscraper: 160 x 600
• • Half-page: 300 x 600
• • Large leaderboard: 970 x 90
• • Billboard: 970 x 250
• • Portrait: 300 x 1050

```html
<!DOCTYPE html>
<html lang="en">
<head>
<meta charset="utf-8">
<title>Plumora Sale PPC Banner Set</title>
<link rel="stylesheet" href="https://fonts.googleapis.com/css2?family=Source+Sans+3:wght@300;400;600;700&display=swap">
<style>
:root{
  --page:#ffffff;
  --ink:#1a1a1a;
  --label:#2b2b2b;
  --sale-red:#e8003f;
  --sale-red-light:#f5154f;
  --sale-red-dark:#a5163a;
  --frame:#3a3a3a;
  --photo-a:#c8182f;
  --photo-b:#e3b51c;
  --photo-c:#2f4f9a;
  --white:#ffffff;
}
*{box-sizing:border-box;margin:0;padding:0}
html,body{width:1200px;height:984px;overflow:hidden;background:var(--page)}
body{position:relative;font-family:"Source Sans 3",Arial,sans-serif;color:var(--ink)}

.size-list{position:absolute;left:85px;top:38px;list-style:none;font-size:26px;line-height:33px;color:var(--label)}

.ad{position:absolute;overflow:hidden;border:1px solid var(--frame);background:var(--white)}
.ad-label{position:absolute;font-size:26px;color:var(--label);white-space:nowrap}

.photo{position:absolute;background:
  linear-gradient(180deg,rgba(47,79,154,.85) 0%,rgba(47,79,154,.35) 28%,rgba(0,0,0,0) 45%),
  linear-gradient(135deg,var(--photo-a) 0%,var(--photo-b) 30%,var(--photo-c) 55%,var(--photo-a) 80%,var(--photo-b) 100%)}

.logo{position:absolute;font-weight:600;color:var(--ink);white-space:nowrap;letter-spacing:-.5px}
.kicker{position:absolute;color:var(--white);font-weight:400;letter-spacing:2px;text-transform:uppercase;white-space:nowrap;line-height:1.1}
.sale{position:absolute;color:var(--white);font-weight:400;letter-spacing:4px;line-height:1;white-space:nowrap}
.cta{position:absolute;background:var(--sale-red-dark);color:var(--white);font-weight:400;display:flex;align-items:center;justify-content:center;text-align:center;line-height:1.1;white-space:nowrap}
.cta b{font-weight:700}

/* Banner 468 x 60 */
.ad-banner{left:101px;top:342px;width:432px;height:56px}
.ad-banner .photo{left:120px;top:0;width:312px;height:100%}
.ad-banner .fade-white{position:absolute;left:0;top:0;width:170px;height:100%;background:linear-gradient(100deg,var(--white) 72%,rgba(255,255,255,0) 100%)}
.ad-banner .fade-red{position:absolute;left:250px;top:0;width:182px;height:100%;background:linear-gradient(100deg,rgba(232,0,63,0) 0%,var(--sale-red) 30%,var(--sale-red-light) 100%)}
.ad-banner .logo{left:22px;top:11px;font-size:28px}
.ad-banner .kicker{left:264px;top:4px;font-size:11px}
.ad-banner .sale{left:276px;top:17px;font-size:36px}
.ad-banner .cta{right:5px;top:6px;width:44px;height:40px;font-size:13px;flex-direction:column;background:var(--sale-red)}

/* Large mobile banner 320 x 100 */
.ad-mobile{left:616px;top:342px;width:296px;height:93px}
.ad-mobile .photo{left:47px;top:0;width:249px;height:100%}
.ad-mobile .logo-strip{position:absolute;left:0;top:0;width:47px;height:100%;background:var(--white)}
.ad-mobile .logo{left:23px;top:46px;font-size:24px;transform:translate(-50%,-50%) rotate(-90deg)}
.ad-mobile .fade-red{position:absolute;left:150px;top:0;width:146px;height:100%;background:linear-gradient(100deg,rgba(232,0,63,0) 0%,var(--sale-red) 28%,var(--sale-red-light) 100%)}
.ad-mobile .kicker{left:171px;top:13px;font-size:12px}
.ad-mobile .sale{left:176px;top:32px;font-size:38px}
.ad-mobile .cta{left:185px;bottom:0;width:111px;height:20px;font-size:13px;background:linear-gradient(90deg,var(--sale-red) 0%,var(--sale-red-dark) 100%)}

/* Square family */
.ad-square .photo{left:0;width:100%}
.ad-square .top{position:absolute;left:0;top:0;width:100%;background:var(--white)}
.ad-square .curve{position:absolute;left:0;width:100%;display:block}
.ad-square .logo{left:0;width:100%;text-align:center}
.ad-square .band{position:absolute;left:0;bottom:0;width:100%;background:var(--sale-red)}
.ad-square .cta{right:0;top:0;height:100%;background:linear-gradient(90deg,var(--sale-red) 0%,var(--sale-red-dark) 100%)}

.ad-small{left:101px;top:579px;width:185px;height:185px}
.ad-small .top{height:38px}
.ad-small .curve{top:37px;height:10px}
.ad-small .logo{top:6px;font-size:28px}
.ad-small .photo{top:40px;height:100px}
.ad-small .band{height:45px}
.ad-small .kicker{left:13px;top:9px;font-size:8px;letter-spacing:1px}
.ad-small .sale{left:20px;top:19px;font-size:24px;letter-spacing:3px}
.ad-small .cta{width:88px;font-size:13px}

.ad-rect{left:425px;top:579px;width:311px;height:259px}
.ad-rect .top{height:48px}
.ad-rect .curve{top:47px;height:12px}
.ad-rect .logo{top:8px;font-size:32px}
.ad-rect .photo{top:50px;height:170px}
.ad-rect .band{height:41px}
.ad-rect .kicker{left:16px;top:6px;font-size:12px}
.ad-rect .sale{left:77px;top:3px;font-size:36px}
.ad-rect .cta{width:124px;font-size:19px}

.ad-large{left:911px;top:579px;width:231px;height:231px}
.ad-large .top{height:38px}
.ad-large .curve{top:37px;height:10px}
.ad-large .logo{top:6px;font-size:30px}
.ad-large .photo{top:40px;height:150px}
.ad-large .band{height:44px}
.ad-large .kicker{left:6px;top:9px;font-size:10px;letter-spacing:1.5px}
.ad-large .sale{left:58px;top:6px;font-size:31px;letter-spacing:3px}
.ad-large .cta{width:92px;font-size:15px}
</style>
</head>
<body>

<ul class="size-list">
  <li>- • Banner: 468 x 60</li>
  <li>- • Large mobile banner 320 x 100</li>
  <li>- • Leaderboard: 728 x 90</li>
  <li>- • Square: 250 x 250</li>
  <li>- • Small square: 200 x 200</li>
  <li>- • Large rectangle: 336 x 280</li>
</ul>

<!-- Banner 468 x 60 -->
<div class="ad ad-banner">
  <div class="photo" role="img" aria-label="Product shot: two-tone loafer on a colourful patterned rug"></div>
  <div class="fade-white"></div>
  <div class="fade-red"></div>
  <div class="logo">Plumora</div>
  <div class="kicker">Luxury Shoes</div>
  <div class="sale">SALE</div>
  <div class="cta"><span>SHOP</span><b>NOW</b></div>
</div>
<div class="ad-label" style="left:102px;top:419px">Banner: 468 x 60</div>

<!-- Large mobile banner 320 x 100 -->
<div class="ad ad-mobile">
  <div class="photo" role="img" aria-label="Product shot: two-tone loafer on a colourful patterned rug"></div>
  <div class="logo-strip"></div>
  <div class="logo">Plumora</div>
  <div class="fade-red"></div>
  <div class="kicker">Luxury Shoes</div>
  <div class="sale">SALE</div>
  <div class="cta"><span>SHOP&nbsp;<b>NOW</b></span></div>
</div>
<div class="ad-label" style="left:616px;top:444px">Large mobile banner 320 x 100</div>

<!-- Small square 200 x 200 -->
<div class="ad ad-square ad-small">
  <div class="photo" role="img" aria-label="Product shot: two-tone loafer on a colourful patterned rug"></div>
  <div class="top"></div>
  <svg class="curve" viewBox="0 0 100 10" preserveAspectRatio="none" aria-hidden="true"><path d="M0 0H100V3Q50 14 0 3Z" fill="#fff"/></svg>
  <div class="logo">Plumora</div>
  <div class="band">
    <div class="kicker">Luxury Shoes</div>
    <div class="sale">SALE</div>
    <div class="cta"><span>SHOP&nbsp;<b>NOW</b></span></div>
  </div>
</div>
<div class="ad-label" style="left:101px;top:783px">Small square: 200 x 200</div>

<!-- Large rectangle 336 x 280 -->
<div class="ad ad-square ad-rect">
  <div class="photo" role="img" aria-label="Product shot: two-tone loafer on a colourful patterned rug"></div>
  <div class="top"></div>
  <svg class="curve" viewBox="0 0 100 10" preserveAspectRatio="none" aria-hidden="true"><path d="M0 0H100V3Q50 14 0 3Z" fill="#fff"/></svg>
  <div class="logo">Plumora</div>
  <div class="band">
    <div class="kicker">Luxury<br>Shoes</div>
    <div class="sale">SALE</div>
    <div class="cta"><span>SHOP&nbsp;<b>NOW</b></span></div>
  </div>
</div>
<div class="ad-label" style="left:423px;top:846px">Large rectangle: 336 x 280</div>

<!-- Square 250 x 250 -->
<div class="ad ad-square ad-large">
  <div class="photo" role="img" aria-label="Product shot: two-tone loafer on a colourful patterned rug"></div>
  <div class="top"></div>
  <svg class="curve" viewBox="0 0 100 10" preserveAspectRatio="none" aria-hidden="true"><path d="M0 0H100V3Q50 14 0 3Z" fill="#fff"/></svg>
  <div class="logo">Plumora</div>
  <div class="band">
    <div class="kicker">Luxury<br>Shoes</div>
    <div class="sale">SALE</div>
    <div class="cta"><span>SHOP&nbsp;<b>NOW</b></span></div>
  </div>
</div>
<div class="ad-label" style="left:911px;top:816px">Square: 250 x 250</div>

</body>
</html>
```